Valtesh Spinal Care and Performance

We need new business cards, something more modern, clean. On the back of the card maybe a quote. The Dr. likes, “The doctor of the future will give no medicine, but will interest his patient in the care of the human frame, in diet and in the cause and prevention of disease.” - Walter Pimsley. We are open to other suggestions. We are a chiropractic office.

```html
<!DOCTYPE html>
<html lang="en">
<head>
<meta charset="utf-8">
<title>Valtesh Spinal Care and Performance – Business Card</title>
<link href="https://fonts.googleapis.com/css2?family=Lato:wght@400;700&family=Roboto:wght@400&display=swap" rel="stylesheet">
<style>
  :root {
    --backdrop: #2b2b2c;
    --card: #1d1e20;
    --card-pattern: #27282b;
    --green: #9dbb1e;
    --purple: #8a3a9c;
    --text: #d9d9d9;
    --rule: #7a7a7a;
  }
  * { margin: 0; padding: 0; box-sizing: border-box; }
  html, body { width: 1200px; height: 1108px; overflow: hidden; }
  body {
    background: var(--backdrop);
    font-family: "Lato", sans-serif;
    color: var(--text);
    position: relative;
  }
  .card {
    position: absolute;
    top: 214px;
    width: 390px;
    height: 680px;
    background: var(--card);
    border-radius: 22px;
    box-shadow: 0 18px 40px rgba(0,0,0,.45);
    overflow: hidden;
  }
  .card--front { left: 170px; text-align: center; }
  .card--back { left: 640px; }

  .brand {
    margin-top: 92px;
    display: flex;
    align-items: center;
    justify-content: center;
    gap: 14px;
  }
  .brand__dot {
    width: 22px; height: 22px; border-radius: 50%;
    background: var(--green);
  }
  .brand__name {
    font-size: 58px;
    font-weight: 400;
    color: var(--purple);
    letter-spacing: 1px;
  }
  .brand__tagline {
    margin-top: 6px;
    font-size: 15px;
    color: var(--purple);
    letter-spacing: 1px;
  }

  .doctor {
    margin-top: 90px;
    font-size: 24px;
    color: var(--green);
    letter-spacing: .5px;
  }

  .divider {
    display: flex;
    align-items: center;
    justify-content: center;
    gap: 10px;
    margin: 30px auto 14px;
    width: 290px;
  }
  .divider::before, .divider::after {
    content: "";
    flex: 1;
    height: 1px;
    background: var(--rule);
  }
  .divider__icon {
    width: 22px; height: 22px; border-radius: 50%;
    background: var(--green);
    display: flex; align-items: center; justify-content: center;
  }
  .divider__icon svg { width: 12px; height: 12px; }

  .contact { font-size: 20px; line-height: 1.35; }
  .address-rule { width: 280px; height: 1px; background: var(--rule); margin: 12px auto; }
  .social { font-size: 20px; }

  .back__pattern {
    position: absolute; inset: 0 0 auto 0; height: 420px;
    background: linear-gradient(180deg, var(--card-pattern), var(--card));
  }
  .back__mark {
    position: absolute; top: 420px; left: 0; right: 0;
    display: flex; align-items: center; justify-content: center; gap: 10px;
    color: var(--green); font-size: 22px;
  }
  .back__mark-dot { width: 18px; height: 18px; border-radius: 50%; background: var(--green); }
  .quote {
    position: absolute; top: 478px; left: 30px; right: 30px;
    font-family: "Roboto", sans-serif;
    font-size: 20px; line-height: 1.3; color: #f2f2f2;
    text-align: center;
  }
  .quote__author { display: block; margin-top: 4px; }
</style>
</head>
<body>
  <section class="card card--front">
    <div class="brand">
      <span class="brand__name">Valtesh</span>
      <span class="brand__dot"></span>
    </div>
    <div class="brand__tagline">SPINAL CARE &amp; PERFORMANCE</div>

    <div class="doctor">DR. JR VALTESH</div>

    <div class="divider">
      <span class="divider__icon"><svg viewBox="0 0 12 12"><path d="M3 1l2 2-1 1.5c.6 1.4 1.6 2.4 3 3L8.5 6.5l2 2L9 10.5C5 10 2 7 1.5 3z" fill="#1d1e20"/></svg></span>
      <span class="divider__icon"><svg viewBox="0 0 12 12"><rect x="1.5" y="3" width="9" height="6" fill="#1d1e20"/><path d="M1.5 3l4.5 3.5L10.5 3" stroke="#9dbb1e" fill="none"/></svg></span>
      <span class="divider__icon"><svg viewBox="0 0 12 12"><circle cx="6" cy="6" r="4.5" fill="none" stroke="#1d1e20" stroke-width="1.3"/><path d="M1.5 6h9M6 1.5c-2 2.5-2 6.5 0 9M6 1.5c2 2.5 2 6.5 0 9" stroke="#1d1e20" fill="none"/></svg></span>
    </div>

    <div class="contact">
      <div>555-014-2286</div>
      <div>jr@valteshspinalcare.com</div>
      <div>www.valteshspinalcare.com</div>
    </div>
    <div class="address-rule"></div>
    <div class="contact">
      <div>410 North Linden Court Road, Suite B</div>
      <div>Maplewood, IL 60199</div>
    </div>

    <div class="divider">
      <span class="divider__icon"></span>
    </div>
    <div class="social">@ValteshSpinalCare</div>
  </section>

  <section class="card card--back">
    <div class="back__pattern" role="img" aria-label="Faint repeating brand-mark pattern"></div>
    <div class="back__mark"><span class="back__mark-dot"></span></div>
    <p class="quote">“The doctor of the future will give no medicine but will interest his patient in the care of the human frame in diet and in the cause and prevention of disease.”
      <span class="quote__author">- Walter Pimsley</span>
    </p>
  </section>
</body>
</html>
```